Business card design for Velluto Events, and Event & Entertainment business

The business card design is for a new business venture, Velluto Events. This company offers Event management, entertainment management and also Latin dance tuition. We currently run Latin dance festivals in Australia & also teach street Latin. This business card is for the director, Mara Dunhill. The Logo has already been designed. So, I need the new design to incorporate and go with the existing Logo.

The look I like is clean, simple & elegant but I also want it to be sexy. Elegant, but not corporate. Clean & simple but not boring :-)

If you want to add another design element as well as using the Logo, please use something with movement. I like ripples or swirls for example.

I would also like to have part of the card embossed or Spot UV pressed so I would like some part of the design to have texture.

Text for the Cards is as follows;

Velluto Events ( Logo attached )

Mara Dunhill

EVENTS & ENTERTAINMENT MANAGEMENT

m: 0478 352 601
e: mara@vellutoevents.com.au
f Velluto Events

www.vellutoevents.com.au

Please try portrait layout.

Thanks, Mara
Updates

Hello Designers, Thank you to all of you who have submitted designs for Velluto Events. I will make up my mind now from what I have already been sent. Very close to making a decision :-) Thank you, Mara

Target Market(s)

Adults, 18 - 60 age group. People who are active. People interested in different cultures. People who like to travel. Please who like to have fun. People who are passionate about Latin dance.

Industry/Entity Type

Entertainment

Font styles to use
Sans Serif
Script

Colors
9bcb3c
ec1f27
ffffff

Requirements
Must have
• Logo + All text listed in brief
Nice to have
• An extra design feature or background image that could be embossed or spot uv pressed to add texture & flare.

```html
<!DOCTYPE html>
<html lang="en">
<head>
<meta charset="utf-8">
<title>Velluto Events – Business Card</title>
<link rel="stylesheet" href="https://fonts.googleapis.com/css2?family=Arimo:wght@400;700&display=swap">
<style>
  :root {
    --lime: #9bcb3c;
    --chili: #ec1f27;
    --white: #ffffff;
    --ink: #3b3b3b;
    --edge: #111111;
    --dash-grey: #666666;
  }
  * { margin: 0; padding: 0; box-sizing: border-box; }
  html, body {
    width: 1200px; height: 1134px; overflow: hidden;
    background: var(--white);
    font-family: "Arimo", Arial, sans-serif;
  }
  .canvas { position: relative; width: 1200px; height: 1134px; }

  .card {
    position: absolute;
    border: 2px solid var(--edge);
    border-radius: 14px;
    overflow: hidden;
    box-shadow: 2px 3px 4px rgba(0,0,0,.35);
  }
  .card--front { left: 60px; top: 138px; width: 471px; height: 853px; background: var(--white); }
  .card--back  { left: 648px; top: 138px; width: 464px; height: 851px; background: var(--chili); }

  .stripe {
    position: absolute; left: 0; width: 100%;
    background: var(--lime);
    box-shadow: 0 2px 2px rgba(0,0,0,.25);
  }
  .tagline {
    position: absolute; left: 0; top: 20px; width: 100%;
    text-align: center; color: var(--white);
    font-size: 26px; line-height: 32px; letter-spacing: .3px;
  }
  .website {
    position: absolute; left: 0; bottom: 34px; width: 100%;
    text-align: center; color: var(--white);
    font-size: 21px; font-weight: 700;
  }

  .mark-art { position: absolute; left: 0; top: 0; }
  .ring--front { fill: var(--white); stroke: var(--lime); stroke-width: 16; }
  .ring--back  { fill: none; stroke: var(--lime); stroke-width: 13; }
  .ring-shadow { fill: none; stroke: rgba(0,0,0,.22); stroke-width: 16; }
  .dash--grey { stroke: var(--dash-grey); stroke-width: 2; stroke-dasharray: 8 8; }
  .dash--lime { stroke: var(--lime); stroke-width: 3; stroke-dasharray: 9 9; }
  .icon-lime { fill: var(--lime); }
  .icon-ring { fill: none; stroke: var(--lime); stroke-width: 3; }

  .brand-name {
    position: absolute; left: 0; width: 100%;
    text-align: center; color: var(--ink);
    font-size: 50px; font-weight: 700; letter-spacing: .5px;
  }
  .card--front .brand-name { top: 560px; }
  .card--back .brand-name { top: 344px; }

  .person-name {
    position: absolute; left: 0; top: 476px; width: 100%;
    text-align: center; color: var(--white);
    font-size: 62px; letter-spacing: 1px;
    text-shadow: 3px 4px 4px rgba(0,0,0,.55);
  }
  .contact-row {
    position: absolute; left: 56px; display: flex; align-items: center;
    color: var(--white); font-size: 19px; letter-spacing: .2px;
  }
  .contact-row svg { width: 48px; height: 44px; margin-right: 16px; flex: none; }
</style>
</head>
<body>
<div class="canvas">

  <section class="card card--front">
    <div class="stripe" style="top:0;height:97px"></div>
    <div class="stripe" style="top:190px;height:96px"></div>
    <div class="stripe" style="top:380px;height:96px"></div>
    <div class="stripe" style="top:570px;height:96px"></div>
    <div class="stripe" style="top:759px;height:94px"></div>

    <p class="tagline">EVENTS &amp; ENTERTAINMENT<br>MANAGEMENT</p>

    <svg class="mark-art" width="471" height="853" viewBox="0 0 471 853" aria-hidden="true">
      <line class="dash--grey" x1="2" y1="428" x2="100" y2="428"/>
      <line class="dash--grey" x1="378" y1="428" x2="471" y2="428"/>
      <circle class="ring-shadow" cx="238" cy="420" r="118"/>
      <circle class="ring--front" cx="236" cy="417" r="118"/>
    </svg>
    <p class="brand-name">Velluto Events</p>

    <p class="website">www.vellutoevents.com.au</p>
  </section>

  <section class="card card--back">
    <svg class="mark-art" width="464" height="851" viewBox="0 0 464 851" aria-hidden="true">
      <line class="dash--lime" x1="0" y1="190" x2="100" y2="190"/>
      <line class="dash--lime" x1="360" y1="190" x2="464" y2="190"/>
      <circle class="ring--back" cx="237" cy="184" r="121"/>
    </svg>
    <p class="brand-name">Velluto Events</p>

    <p class="person-name">Mara Dunhill</p>

    <div class="contact-row" style="top:616px">
      <svg viewBox="0 0 48 44" aria-hidden="true">
        <circle class="icon-ring" cx="24" cy="22" r="19"/>
      </svg>
      <span>Velluto Events</span>
    </div>
    <div class="contact-row" style="top:688px">
      <svg viewBox="0 0 48 44" aria-hidden="true">
        <path class="icon-lime" d="M13 8c3-2 5-1 6 1l3 6c1 2 0 3-2 4l-2 1c1 4 5 9 9 11l1-2c1-2 3-2 4-1l6 4c2 1 2 3 0 5-3 3-6 4-10 2-8-4-14-11-17-19-1-5 0-9 2-12z"/>
      </svg>
      <span>0478 352 601</span>
    </div>
    <div class="contact-row" style="top:752px">
      <svg viewBox="0 0 48 44" aria-hidden="true">
        <rect class="icon-lime" x="8" y="12" width="30" height="20"/>
        <path d="M8 12l15 12 15-12M8 32l11-10M38 32l-11-10" fill="none" stroke="#2f6b1e" stroke-width="1.6"/>
      </svg>
      <span>mara@vellutoevents.com.au</span>
    </div>
  </section>

</div>
</body>
</html>
```